Flyer for a Business Consultant

I need a one-page description of services. I am a Brinmore Accredited Talents Mentor. I do not have a personal website but think I will soon purchase this template https://quillerlayouts.example/layouts/lectern/. I like the larger font, simplicity and larger font. I will attach his pricing flyer which I like - not to overly guide or restrict your creative thinking, but only to give a little perspective. I don't like busy, noisy - I like clarity, simplicity. Here 's the Brinmore website which these same traits https://www.brinmoretalentshub.example/ and can be a source of ideas and colors.

Target Market(s)

CEOs and Middle Managers in organizations

Industry/Entity Type

Financial Service

Colors

Designer to choose colors to be used in the design.

Requirements
Must have
• Clarity, simplicity, but also strength (not weak or frilly looking)
Nice to have
• Warm color(s), larger/not skinny font
Should not have
• Loud, noisy, busy

```html
<!DOCTYPE html>
<html lang="en">
<head>
<meta charset="utf-8">
<title>Dorian Ashcombe – Team Effectiveness Flyer</title>
<link href="https://fonts.googleapis.com/css2?family=Montserrat:wght@400;500;700;800&display=swap" rel="stylesheet">
<style>
  :root {
    --teal: #2fb5a3;
    --teal-deep: #1c7f76;
    --teal-dark: #0f4f4c;
    --navy: #1f2d45;
    --ink: #111417;
    --body: #3a3f45;
    --page: #f2f2f0;
    --paper: #f7f8f8;
    --white: #ffffff;
  }
  * { box-sizing: border-box; margin: 0; padding: 0; }
  html, body { width: 1200px; height: 797px; overflow: hidden; }
  body {
    background: var(--page);
    font-family: "Montserrat", Arial, sans-serif;
    color: var(--body);
  }
  .flyer {
    position: absolute;
    left: 318px; top: 0;
    width: 564px; height: 797px;
    background: linear-gradient(180deg, var(--white) 0%, var(--paper) 60%, #eef0f0 100%);
    overflow: hidden;
  }
  .hero {
    position: absolute; left: 0; top: 0;
    width: 564px; height: 300px;
    background: linear-gradient(160deg, #3ec2b0 0%, var(--teal) 35%, var(--teal-deep) 75%, var(--teal-dark) 100%);
  }
  .brand {
    position: absolute; left: 23px; top: 30px;
    display: flex; align-items: center; gap: 7px;
    font-family: "Montserrat", Arial, sans-serif;
    font-weight: 700; font-size: 15px;
    color: var(--white);
  }
  .brand-square { width: 10px; height: 10px; background: var(--white); display: block; }
  .headline {
    position: absolute; left: 75px; top: 170px; width: 470px;
    font-weight: 800; font-size: 26px; line-height: 29px;
    color: var(--white); letter-spacing: -0.6px;
  }
  .benefits {
    position: absolute; left: 31px; top: 247px;
    width: 503px; height: 110px;
    background: var(--white);
    box-shadow: 0 4px 14px rgba(0,0,0,0.08);
  }
  .benefits h2 {
    position: absolute; left: 44px; top: 20px;
    font-size: 15.5px; font-weight: 700; color: var(--ink);
  }
  .benefit {
    position: absolute; top: 48px;
    font-size: 9px; line-height: 10.5px; color: var(--body);
    padding-left: 17px;
  }
  .benefit svg { position: absolute; left: 0; top: 0; }
  .benefit-1 { left: 44px; width: 140px; }
  .benefit-2 { left: 207px; width: 135px; }
  .benefit-3 { left: 356px; width: 115px; }
  .service { position: absolute; left: 75px; width: 412px; }
  .service h3 {
    font-size: 13px; font-weight: 700; color: var(--ink); letter-spacing: -0.3px;
  }
  .service .rule {
    width: 13px; height: 2px; background: var(--teal);
    margin: 7px 0 14px;
  }
  .service p { font-size: 8.8px; line-height: 10.5px; color: var(--body); }
  .service-individual { top: 386px; }
  .service-workshop { top: 483px; }
  .service-followon { top: 589px; }
  .contact {
    position: absolute; left: 0; top: 710px;
    width: 564px; height: 87px;
    background: var(--navy); color: var(--white);
  }
  .contact .name { position: absolute; left: 31px; top: 21px; font-size: 11px; font-weight: 700; }
  .contact .role { position: absolute; left: 31px; top: 33px; font-size: 11.5px; font-weight: 500; }
  .contact .line {
    position: absolute; left: 31px; font-size: 9.5px; font-weight: 500;
    display: flex; align-items: center; gap: 4px;
  }
  .contact .email { top: 50px; }
  .contact .phone { top: 64px; }
  .badge {
    position: absolute; left: 405px; top: 34px;
    width: 130px; height: 36px;
    background: var(--white);
    display: flex; align-items: center; padding-left: 12px;
  }
  .badge span { width: 20px; height: 20px; background: #7b7f84; display: block; }
  .badge i { display: block; margin-left: 8px; width: 82px; height: 14px; background: #d9dbdd; }
</style>
</head>
<body>
  <main class="flyer">
    <header class="hero" role="img" aria-label="Teal-toned photo of a team of colleagues in discussion around a meeting table">
      <div class="brand"><span class="brand-square"></span>Dorian Ashcombe</div>
      <h1 class="headline">A Strength-Based Approach To Managing Team Effectiveness</h1>
    </header>

    <section class="benefits">
      <h2>We Help Teams Grow Stronger By:</h2>
      <p class="benefit benefit-1">
        <svg width="11" height="11" viewBox="0 0 11 11"><circle cx="5.5" cy="5.5" r="5.5" fill="#2fb5a3"/><path d="M3 5.6l1.7 1.7L8 4" fill="none" stroke="#fff" stroke-width="1.4"/></svg>
        Bringing a deep awareness of their strengths and the strengths of their associates.
      </p>
      <p class="benefit benefit-2">
        <svg width="11" height="11" viewBox="0 0 11 11"><circle cx="5.5" cy="5.5" r="5.5" fill="#2fb5a3"/><path d="M3 5.6l1.7 1.7L8 4" fill="none" stroke="#fff" stroke-width="1.4"/></svg>
        Increasing the Team's communication and sense of partnership.
      </p>
      <p class="benefit benefit-3">
        <svg width="11" height="11" viewBox="0 0 11 11"><circle cx="5.5" cy="5.5" r="5.5" fill="#2fb5a3"/><path d="M3 5.6l1.7 1.7L8 4" fill="none" stroke="#fff" stroke-width="1.4"/></svg>
        Improving employee engagement and effectiveness.
      </p>
    </section>

    <section class="service service-individual">
      <h3>Individual sessions</h3>
      <div class="rule"></div>
      <p>Conversational feedback and coaching sessions based on Brinmore's TalentScope assessments. These sessions last about an hour and lead to a personalized translation of the results and how their strengths show up in their work and inherent blind spots they bring.</p>
    </section>

    <section class="service service-workshop">
      <h3>Strength Discovery Workshop</h3>
      <div class="rule"></div>
      <p>A retreat-style Team Workshop in which the team learns each other's unique Top 5 strengths. The session is very interactive and provides a common language that leads to improved communication and effectiveness. Tailored in 2,3 and 4-hour options are tailored to your Team's challenges and opportunities.</p>
    </section>

    <section class="service service-followon">
      <h3>Follow-on modules</h3>
      <div class="rule"></div>
      <p>Follow-on is important to make the insights learned to be practical and integrated into the Teams' approach and workflows. In a debrief session included as part of the workshop, we provide several 15-minute exercise modules for use in regular meetings, and we offer guest facilitated modules of 30-60 minutes each.</p>
    </section>

    <footer class="contact">
      <div class="name">Dorian Ashcombe</div>
      <div class="role">Brinmore Workplace Talents Mentor</div>
      <div class="line email">
        <svg width="11" height="11" viewBox="0 0 11 11"><rect width="11" height="11" rx="1.5" fill="#2fb5a3"/><rect x="2" y="3" width="7" height="5" fill="none" stroke="#fff" stroke-width="0.9"/><path d="M2 3l3.5 2.8L9 3" fill="none" stroke="#fff" stroke-width="0.9"/></svg>
        dorian@talentsfocus.example
      </div>
      <div class="line phone">
        <svg width="11" height="11" viewBox="0 0 11 11"><rect width="11" height="11" rx="1.5" fill="#2fb5a3"/><path d="M3.2 2.3l1.3 1.6-.7.9c.5 1 1.2 1.7 2.2 2.2l.9-.7 1.6 1.3-.8 1.1C5.6 8.6 2.4 5.4 2.1 3.1z" fill="#fff"/></svg>
        555-014-2270
      </div>
      <div class="badge" role="img" aria-label="Accreditation badge">
        <span></span><i></i>
      </div>
    </footer>
  </main>
</body>
</html>
```